Restaurant Finder Website Design

I need to create a website that will help people find restaurants around a zip code or address.

I would like to have a very clean and simple design. I will need a design for the homepage, that should be very clean and simple to use. its where the users will launch their search. I am thinking something like tavlex like.. big search field with a very clean page where users can create an account or restaurants subscribe to the service.

Also need the design of the search results page, I would like to display a big map with the results and a list on the side or the bottom of the map.

Also need a profile page for the users that sign up to the site.

Mostly what I need are guidelines and color coordinated elements, like a general layout and buttons that work together. I would like to know what the action buttons and elements should look like. Because its going to have some more detail pages.

Target Market(s)

People in general, mainly people that work at an office and have to find a place for lunch every day.

Industry/Entity Type

Restaurant

Number of Pages Required

4 page

Font styles to use
Serif
Sans Serif

Requirements
Must have
• It must be a really simple and clean design but look edgy.

```html
<!DOCTYPE html>
<html lang="en">
<head>
<meta charset="utf-8">
<title>Forkway – Search Results</title>
<link rel="stylesheet" href="https://fonts.googleapis.com/css2?family=Roboto:wght@400;500&family=Noto+Serif:wght@600&display=swap">
<style>
:root{
  --page:#f3f7ee;
  --red:#c0202a;
  --red-dark:#b3181f;
  --ink:#1d1d1d;
  --star:#2a7de1;
  --map-light:#e9e3d6;
  --map-dark:#ddd3bf;
  --foot-top:#f47e72;
  --foot-bottom:#ff2d12;
  --white:#ffffff;
}
*{box-sizing:border-box;margin:0;padding:0}
html,body{width:1189px;height:1200px;overflow:hidden}
body{background:var(--page);font-family:"Roboto",Arial,sans-serif;color:var(--ink);position:relative}
.brand{position:absolute;left:107px;top:22px;display:flex;align-items:center;gap:8px}
.brand-dot{width:44px;height:44px;border-radius:50%;background:var(--red)}
.brand-name{font-size:22px;font-weight:500;color:var(--ink)}
.nav{position:absolute;left:0;right:0;top:0;height:110px;border-bottom:1px solid var(--red)}
.nav a{position:absolute;top:66px;font-size:20px;color:var(--red);text-decoration:none;padding-bottom:14px}
.nav a.active{color:var(--ink);border-bottom:4px solid #222}
.search{position:absolute;left:393px;top:135px;width:403px;height:48px;border:1px solid var(--ink);border-radius:8px;display:flex;overflow:hidden;background:var(--white)}
.search-input{flex:1;padding-left:20px;line-height:46px;font-size:16px;color:var(--red)}
.search-btn{width:90px;background:var(--red-dark);color:var(--white);font-size:15px;line-height:46px;text-align:center;border-radius:8px}
.results{position:absolute;left:159px;top:216px;width:872px;height:641px;background:var(--white);box-shadow:0 10px 22px rgba(0,0,0,.35)}
.results h1{text-align:center;font-weight:400;font-size:25px;color:var(--red);margin-top:10px}
.grid{position:absolute;left:27px;top:71px;display:grid;grid-template-columns:repeat(3,231px);column-gap:67px;row-gap:56px}
.map{width:231px;height:195px;border:1px solid #333;border-radius:6px;background:linear-gradient(160deg,var(--map-light),var(--map-dark))}
.meta{position:relative;height:37px;margin-top:12px}
.name{position:absolute;left:0;top:2px;font-size:14px;font-weight:500;color:var(--red)}
.type{position:absolute;left:12px;top:22px;font-size:15px}
.stars{position:absolute;left:132px;top:0;font-size:20px;color:var(--star);letter-spacing:2px}
.footer{position:absolute;left:0;top:949px;width:1189px;height:210px;background:linear-gradient(var(--foot-top),var(--foot-bottom))}
.footer h2{position:absolute;font-size:20px;font-weight:400;color:#111}
.about{left:107px;top:25px}
.about-text{position:absolute;left:111px;top:62px;width:690px;font-family:"Noto Serif",Georgia,serif;font-weight:600;font-size:12.4px;line-height:24.5px;color:var(--white)}
.divider{position:absolute;left:835px;top:33px;width:1px;height:152px;background:var(--red)}
.contact{left:915px;top:25px}
.social{position:absolute;left:872px;top:76px;display:flex;gap:15px}
.social span{width:37px;height:37px;border-radius:3px}
.phone{position:absolute;left:881px;top:148px;font-family:"Noto Serif",Georgia,serif;font-size:20px;color:var(--white)}
.phone-icon{position:absolute;left:1022px;top:143px}
.bottom{position:absolute;left:107px;right:110px;top:1170px;display:flex;justify-content:space-between;font-size:15px;color:var(--red)}
</style>
</head>
<body>
<nav class="nav">
  <a class="active" href="#" style="left:395px">Home</a>
  <a href="#" style="left:516px">Restaurant List</a>
  <a href="#" style="left:721px">Our service</a>
  <a href="#" style="left:892px">Contact Us</a>
</nav>
<div class="brand"><span class="brand-dot"></span><span class="brand-name">Forkway</span></div>

<div class="search"><div class="search-input">Find The Restaurant</div><div class="search-btn">Search</div></div>

<main class="results">
  <h1>Search Results</h1>
  <div class="grid">
    <article><div class="map" role="img" aria-label="Street map with restaurant location pin"></div><div class="meta"><span class="name">Restaurant 1</span><span class="type">Meals</span><span class="stars">★★★★</span></div></article>
    <article><div class="map" role="img" aria-label="Street map with restaurant location pin"></div><div class="meta"><span class="name">Restaurant 1</span><span class="type">Meals</span><span class="stars">★★★★</span></div></article>
    <article><div class="map" role="img" aria-label="Street map with restaurant location pin"></div><div class="meta"><span class="name">Restaurant 1</span><span class="type">Meals</span><span class="stars">★★★★</span></div></article>
    <article><div class="map" role="img" aria-label="Street map with restaurant location pin"></div><div class="meta"><span class="name">Restaurant 1</span><span class="type">Meals</span><span class="stars">★★★★</span></div></article>
    <article><div class="map" role="img" aria-label="Street map with restaurant location pin"></div><div class="meta"><span class="name">Restaurant 1</span><span class="type">Meals</span><span class="stars">★★★★</span></div></article>
    <article><div class="map" role="img" aria-label="Street map with restaurant location pin"></div><div class="meta"><span class="name">Restaurant 1</span><span class="type">Meals</span><span class="stars">★★★★</span></div></article>
  </div>
</main>

<footer class="footer">
  <h2 class="about">About US</h2>
  <p class="about-text">Sed ut perspiciatis unde omnis iste natus error sit voluptatem accusantium doloremque laudantium, totam rem aperiam, eaque ipsa quae ab illo inventore veritatis et quasi architecto beatae vitae dicta sunt explicabo. Nemo enim ipsam voluptatem quia voluptas sit aspernatur aut odit aut fugit, sed quia consequuntur magni dolores eos qui ratione voluptatem sequi nesciunt. Neque porro quisquam est, qui dolorem ipsum quia dolor sit amet, consectetur, adipisci velit, sed quia non numquam eius modi tempora incidunt ut labore et dolore</p>
  <div class="divider"></div>
  <h2 class="contact">Contact Us</h2>
  <div class="social" aria-label="Social links">
    <span style="background:#3b5a9a"></span>
    <span style="background:#2fb2e8"></span>
    <span style="background:#c0202a"></span>
    <span style="background:#dd5040"></span>
  </div>
  <div class="phone">0100 555 0199</div>
  <svg class="phone-icon" width="42" height="34" viewBox="0 0 42 34" aria-label="Phone">
    <path d="M3 12 Q21 -2 39 12 L34 17 L29 12 L13 12 L8 17 Z" fill="#e23b2e" stroke="#7a1510" stroke-width="1"/>
    <path d="M9 16 L33 16 L38 32 L4 32 Z" fill="#f4f4f4" stroke="#555" stroke-width="1"/>
    <circle cx="21" cy="24" r="6" fill="none" stroke="#e23b2e" stroke-width="2"/>
  </svg>
</footer>

<div class="bottom"><span>Add Your Own Footer Text Here</span><span>Copyright 2016 / all rights reserve / Forkway</span></div>
</body>
</html>
```